Norvale Email Signature Banners – Fabrication Capability Series

www.Norvale.com.au is an Australian engineering and fabrication company specialising in fabrication and welding of :
steel piping spools,
skids and frames,
small volume process steel tanks
and general steel fabrication
We require four distinct banner designs for use in Teldrin Quillmark email signatures. Each banner will highlight a specific capability while maintaining a consistent brand identity.
Deliverables
Four banners total:
Piping Spools Fabrication – focus on precision welding and stainless steel pipework
Skid & Frames Fabrication – highlight skid systems and structural frames
Small Steel Tanks Fabrication – show fabricated tanks and workshop craftsmanship
General Fabrication Solutions – broad steel fabrication theme for company-wide use
Dimensions: 600–700 px wide × 100 px high
Format: PNG (preferred), small file size prefered
Resolution: 72 dpi
Background: non-transparent, industrial or workshop setting
Text examples:
1. Piping Spools Fabrication
Option A: “Expert Fabrication Solutions for Process Piping”
Option B: “Precision Welding for Complex Systems”
Option C: “Delivering Quality in Every Spool”
Option D: “Engineered for Flow, Built for Strength”
2. Skid & Frames Fabrication
Option A: “Custom Engineered Modular Systems”
Option B: “Built Strong. Designed Smart.”
Option C: “Reliable Frames for Industrial Performance”
Option D: “Modular Fabrication for Seamless Integration”
3. Small Steel Tanks Fabrication
Option A: “Precision Built for Your Needs”
Option B: “Compact Strength. Proven Durability.”
Option C: “Fabricated for Performance and Longevity”
Option D: “Small Tanks. Big Reliability.”
4. General Fabrication Solutions
Option A: “Quality Craftsmanship, Proven Results”
Option B: “Your Partner in Precision Fabrication”
Option C: “Engineering Excellence in Every Weld”
Option D: “Australian Fabrication. Global Standards.”
Style Direction
Clean, professional, and engineering‑focused
Use Norvale brand colours
Blend photo realism with vector clarity (no heavy gradients)
Include subtle industrial textures or workshop imagery
Typography: bold sans‑serif, legible at small scale
Usage Context
These banners will appear at the bottom of staff email signatures via Quillmark Email Signature Tool for Teldrin 365, so clarity and fast loading are essential. No Logo is required in the banners.
Reference
Existing Norvale signature is attached. Colour palette to match the signature style and logo.
Target Market(s)
Engineering and construction companies,
Industry/Entity Type
Engineering fabrication design

```html
<!DOCTYPE html>
<html lang="en">
<head>
<meta charset="UTF-8">
<title>Norvale – Skid &amp; Frames Fabrication Banner</title>
<link rel="stylesheet" href="https://fonts.googleapis.com/css2?family=Montserrat:wght@500;700&display=swap">
<style>
  :root {
    --brand-blue: #1ca3dc;
    --white: #ffffff;
    --skid-green-dark: #1f5a3c;
    --skid-green: #2f7a52;
    --sky: #9ec4dc;
    --plant-grey-light: #c9cdd0;
    --plant-grey-dark: #5e656b;
  }
  html, body {
    margin: 0;
    padding: 0;
    width: 1200px;
    height: 171px;
    overflow: hidden;
    background: var(--white);
  }
  .banner {
    position: relative;
    width: 1200px;
    height: 171px;
    background: var(--brand-blue);
    font-family: "Montserrat", Arial, sans-serif;
    color: var(--white);
  }
  .banner-shapes {
    position: absolute;
    inset: 0;
  }
  .banner-copy {
    position: absolute;
    left: 317px;
    width: 566px;
    top: 0;
    height: 171px;
    text-align: center;
  }
  .headline {
    position: absolute;
    left: 0;
    right: 0;
    top: 47px;
    margin: 0;
    font-weight: 700;
    font-size: 32px;
    line-height: 1;
    letter-spacing: 0;
    white-space: nowrap;
  }
  .divider {
    position: absolute;
    left: 129px;
    width: 303px;
    top: 97px;
    height: 2px;
    background: var(--white);
  }
  .subline {
    position: absolute;
    left: 0;
    right: 0;
    top: 117px;
    margin: 0;
    font-weight: 500;
    font-size: 23px;
    line-height: 1;
    white-space: nowrap;
  }
</style>
</head>
<body>
  <div class="banner">
    <svg class="banner-shapes" width="1200" height="171" viewBox="0 0 1200 171">
      <defs>
        <linearGradient id="skidPhotoTone" x1="0" y1="0" x2="0" y2="1">
          <stop offset="0" stop-color="var(--sky)"/>
          <stop offset="0.35" stop-color="var(--skid-green)"/>
          <stop offset="1" stop-color="var(--skid-green-dark)"/>
        </linearGradient>
        <linearGradient id="plantPhotoTone" x1="0" y1="0" x2="1" y2="1">
          <stop offset="0" stop-color="var(--plant-grey-light)"/>
          <stop offset="1" stop-color="var(--plant-grey-dark)"/>
        </linearGradient>
      </defs>

      <polygon class="photo-skid" role="img"
        aria-label="Photo of a green fabricated process skid with pipework in an outdoor yard"
        points="0,0 291,0 317,85.5 291,171 0,171"
        fill="url(#skidPhotoTone)"/>
      <polyline class="chevron-edge" points="291,0 317,85.5 291,171"
        fill="none" stroke="var(--white)" stroke-width="6"/>

      <polygon class="photo-plant" role="img"
        aria-label="Photo of stainless steel pipework and structural frames inside an industrial plant"
        points="909,0 1200,0 1200,171 909,171 883,85.5"
        fill="url(#plantPhotoTone)"/>
      <polyline class="chevron-edge" points="909,0 883,85.5 909,171"
        fill="none" stroke="var(--white)" stroke-width="6"/>
    </svg>

    <div class="banner-copy">
      <h1 class="headline">Built Strong. Designed Smart</h1>
      <div class="divider"></div>
      <p class="subline">Skid &amp; Frames Fabrication</p>
    </div>
  </div>
</body>
</html>
```